Multiple Packaging Solutions for LED bulbs

We need a packaging design for led bulbs for our company. We need something that can be easily adjusted in different packaging types, as we have multiple different products. It needs to be fresh, friendly, happy but at the same time corporate. We provide some basic packaging dimensions and also our logo in the respective files. The packaging could be of plastic/trasparent, or carton (regular or ecofriendly)

Industry/Entity Type

It Company

```html
<!DOCTYPE html>
<html lang="en">
<head>
<meta charset="utf-8">
<title>Lumora LED Bulb Carton – Dieline</title>
<link rel="stylesheet" href="https://fonts.googleapis.com/css2?family=Open+Sans:wght@300;400;600;700&family=Montserrat:wght@600;700&display=swap">
<style>
  :root {
    --paper: #ffffff;
    --cut-line: #8cc63f;
    --fold-line: #e8403a;
    --dimension: #2b7bbf;
    --magenta: #c4238f;
    --ink-dark: #333333;
    --ink-grey: #555555;
    --white: #ffffff;
    --warm-orange: #f7a21b;
    --warm-red: #ec5a4e;
    --warm-pink: #f06a7e;
  }
  html, body {
    margin: 0;
    padding: 0;
    width: 1200px;
    height: 1126px;
    overflow: hidden;
    background: var(--paper);
  }
  .dieline {
    display: block;
    width: 1200px;
    height: 1126px;
  }
  .dim-text { font-family: "Open Sans", sans-serif; font-size: 9px; fill: var(--dimension); }
  .dim-line { stroke: var(--dimension); stroke-width: 0.6; fill: none; }
  .dim-guide { stroke: #9fc9e8; stroke-width: 0.5; fill: none; }
  .cut { stroke: var(--cut-line); stroke-width: 1; fill: none; }
  .fold { stroke: var(--fold-line); stroke-width: 0.8; fill: none; }
  .wordmark { font-family: "Open Sans", sans-serif; font-weight: 300; letter-spacing: 1px; }
  .spec-number { font-family: "Montserrat", sans-serif; font-weight: 700; }
  .spec-label { font-family: "Open Sans", sans-serif; font-weight: 600; letter-spacing: 0.3px; }
  .variant { font-family: "Open Sans", sans-serif; font-weight: 400; letter-spacing: 0.5px; }
</style>
</head>
<body>
<svg class="dieline" viewBox="0 0 900 845" xmlns="http://www.w3.org/2000/svg">
  <defs>
    <linearGradient id="lid-shade" x1="0" y1="0" x2="0" y2="1">
      <stop offset="0" stop-color="#000000"/>
      <stop offset="0.3" stop-color="#111111"/>
      <stop offset="1" stop-color="#8a8a8a"/>
    </linearGradient>
    <radialGradient id="front-shade" cx="0.5" cy="0.72" r="0.75">
      <stop offset="0" stop-color="#f7f7f7"/>
      <stop offset="0.55" stop-color="#d0d0d0"/>
      <stop offset="1" stop-color="#8f8f8f"/>
    </radialGradient>
    <linearGradient id="warm-glow" x1="0" y1="0" x2="1" y2="1">
      <stop offset="0" stop-color="#ec5a4e" stop-opacity="0.55"/>
      <stop offset="0.5" stop-color="#f57d30" stop-opacity="0.45"/>
      <stop offset="1" stop-color="#f7a21b" stop-opacity="0.5"/>
    </linearGradient>
    <linearGradient id="magenta-glow" x1="0" y1="0" x2="1" y2="1">
      <stop offset="0" stop-color="#f7a21b" stop-opacity="0.75"/>
      <stop offset="0.55" stop-color="#f07a45" stop-opacity="0.5"/>
      <stop offset="1" stop-color="#f06a7e" stop-opacity="0.55"/>
    </linearGradient>
    <radialGradient id="bulb-soft" cx="0.5" cy="0.4" r="0.6">
      <stop offset="0" stop-color="#ffffff"/>
      <stop offset="1" stop-color="#c9c9c9"/>
    </radialGradient>
  </defs>

  <!-- Dimensions -->
  <g class="dimensions">
    <line class="dim-guide" x1="110" y1="12" x2="110" y2="272"/>
    <line class="dim-guide" x1="292" y1="12" x2="292" y2="52"/>
    <line class="dim-guide" x1="473" y1="12" x2="473" y2="52"/>
    <line class="dim-line" x1="112" y1="20" x2="290" y2="20"/>
    <path d="M110,20 l5,-2.5 v5 z M292,20 l-5,-2.5 v5 z" fill="var(--dimension)"/>
    <rect x="175" y="14" width="50" height="12" fill="var(--paper)"/>
    <text class="dim-text" x="200" y="23.5" text-anchor="middle">64.00 mm</text>
    <line class="dim-line" x1="294" y1="14" x2="471" y2="14"/>
    <path d="M292,14 l5,-2.5 v5 z M473,14 l-5,-2.5 v5 z" fill="var(--dimension)"/>
    <rect x="357" y="8" width="50" height="12" fill="var(--paper)"/>
    <text class="dim-text" x="382" y="17.5" text-anchor="middle">64.00 mm</text>
    <line class="dim-guide" x1="30" y1="272" x2="110" y2="272"/>
    <line class="dim-guide" x1="30" y1="660" x2="110" y2="660"/>
    <line class="dim-line" x1="38" y1="274" x2="38" y2="658"/>
    <path d="M38,272 l-2.5,5 h5 z M38,660 l-2.5,-5 h5 z" fill="var(--dimension)"/>
    <rect x="32" y="438" width="12" height="56" fill="var(--paper)"/>
    <text class="dim-text" transform="translate(41,466) rotate(-90)" text-anchor="middle">137.00 mm</text>
  </g>

  <!-- Printed areas -->
  <g class="panel-lid">
    <rect x="292" y="52" width="98" height="220" fill="url(#lid-shade)"/>
    <g transform="rotate(180 340 110)" fill="var(--white)">
      <text class="spec-number" x="340" y="100" font-size="20" text-anchor="middle">9</text>
      <text class="spec-label" x="340" y="112" font-size="9" text-anchor="middle">WATTS</text>
      <text class="spec-number" x="340" y="142" font-size="26" text-anchor="middle">700</text>
      <rect x="303" y="147" width="72" height="2"/>
      <text class="spec-label" x="340" y="161" font-size="10" text-anchor="middle">LUMENS</text>
    </g>
    <g class="lid-brand">
      <text class="wordmark" transform="translate(444,110) rotate(90)" font-size="30" fill="var(--ink-dark)">lumora</text>
      <circle cx="444" cy="240" r="10" fill="var(--warm-orange)"/>
    </g>
  </g>

  <g class="panel-side-left">
    <rect role="img" aria-label="Large warm orange and red light bulb graphic" x="215" y="300" width="77" height="255" rx="38" fill="url(#warm-glow)"/>
    <g class="certification-marks" fill="#6a6a6a">
      <rect x="129" y="632" width="10" height="12" rx="1"/>
      <circle cx="152" cy="638" r="6"/>
      <rect x="163" y="632" width="12" height="12" rx="2"/>
      <circle cx="197" cy="638" r="6"/>
    </g>
  </g>

  <g class="panel-front">
    <rect x="292" y="272" width="98" height="388" fill="url(#front-shade)"/>
    <rect role="img" aria-label="Warm orange and red light bulb graphic continuing from the side panel" x="292" y="300" width="98" height="255" rx="30" fill="url(#warm-glow)"/>
    <rect role="img" aria-label="Illustration of a white LED bulb" x="318" y="525" width="58" height="72" rx="26" fill="url(#bulb-soft)"/>
    <g class="front-specs" fill="var(--ink-grey)">
      <text class="spec-number" x="321" y="634" font-size="14" text-anchor="middle">700</text>
      <text class="spec-label" x="321" y="646" font-size="6.5" text-anchor="middle">LUMENS</text>
      <rect x="346" y="620" width="1" height="30"/>
      <text class="spec-number" x="367" y="634" font-size="14" text-anchor="middle">9</text>
      <text class="spec-label" x="367" y="646" font-size="6.5" text-anchor="middle">WATTS</text>
    </g>
    <g class="front-brand">
      <circle cx="420" cy="335" r="14" fill="var(--warm-orange)"/>
      <text class="wordmark" transform="translate(404,398) rotate(90)" font-size="60" fill="var(--ink-dark)">lumora</text>
    </g>
  </g>

  <g class="panel-back">
    <rect x="473" y="272" width="365" height="388" fill="var(--magenta)"/>
    <polygon points="838,272 864,280 864,652 838,660" fill="var(--magenta)"/>
    <rect role="img" aria-label="Large orange and pink light bulb graphic" x="500" y="290" width="260" height="360" rx="80" fill="url(#magenta-glow)"/>
    <rect role="img" aria-label="Line drawing of an E27 LED bulb" x="660" y="385" width="100" height="185" rx="40" fill="#ffffff" fill-opacity="0.12"/>
    <circle cx="795" cy="335" r="18" fill="var(--white)"/>
    <text class="wordmark" transform="translate(778,398) rotate(90)" font-size="64" fill="var(--white)">lumora</text>
    <text class="variant" transform="translate(760,470) rotate(90)" font-size="15" fill="var(--white)">E27 | COOL LIGHT</text>
    <g class="back-specs" fill="var(--white)">
      <text class="spec-number" x="690" y="634" font-size="14" text-anchor="middle">700</text>
      <text class="spec-label" x="690" y="646" font-size="6.5" text-anchor="middle">LUMENS</text>
      <rect x="714" y="620" width="1" height="30"/>
      <text class="spec-number" x="733" y="634" font-size="14" text-anchor="middle">9</text>
      <text class="spec-label" x="733" y="646" font-size="6.5" text-anchor="middle">WATTS</text>
    </g>
  </g>

  <!-- Cut and fold lines -->
  <g class="cut-lines">
    <path class="cut" d="M110,272 V210 Q110,202 118,202 H280 Q290,202 290,212 L292,272"/>
    <path class="cut" d="M292,272 V52 H455 Q473,52 473,70 V272"/>
    <path class="cut" d="M473,272 V210 Q473,202 481,202 H643 Q653,202 653,212 L655,272"/>
    <path class="cut" d="M110,272 V660"/>
    <path class="cut" d="M110,660 V668 L150,702 V742 Q150,755 163,755 H232 Q245,755 245,742 V702 L292,664"/>
    <path class="cut" d="M292,660 L350,738 V790 H412 V738 L473,660"/>
    <path class="cut" d="M473,660 V755 H525 V728 Q525,718 536,718 H548 L570,735 L600,700 L655,660"/>
    <path class="cut" d="M655,660 V798 H715 V748 H745 V798 H838 V668 L864,660 V280 L838,272"/>
  </g>
  <g class="fold-lines">
    <line class="fold" x1="110" y1="272" x2="864" y2="272"/>
    <line class="fold" x1="390" y1="93" x2="473" y2="93"/>
  </g>
</svg>
</body>
</html>
```